New Corporate Email Signature with Custom GIF Tavik Electric LLC & Tavik Fire & Security

Project Overview
Tavik Electric LLC and Tavik Fire & Security are seeking a professional, polished, and technically robust corporate email signature design. The project has two integrated deliverables:
A custom animated GIF representing both sides of our business
A complete corporate email signature layout designed for real-world compatibility (Gmail, Outlook, iOS, Android)
Our brand aesthetic is corporate, conservative, and clean. We value clarity, trust, professionalism, and subtle creativity β€” nothing overly flashy or cartoonish.
This design will be used across the entire company and must be visually aligned with our brand while remaining technically dependable.

PART 1 β€” Animated GIF Requirements
The GIF will be the core visual anchor of the new signature.
It must be clean, smooth, subtle, and optimized for email use.
βš™ Technical Requirements
Max file size: 150–200 KB (smaller is better)
Dimensions: approx 300px width (flexible, but must look good small)
Looping: continuous loop
Style: professional, minimalistic transitions

No rapid flashing or harsh animations
Must export cleanly into a format email clients accept

🎞 GIF Animation Sequence
Phase 1 β€” Tavik Electric (TE)
Use the yellow β€œTE” avatar logo (provided).
Animation flow:
TE avatar appears
Full name β€œTavik Electric LLC” slides in, fades in, or otherwise appears smoothly
A scrolling or cycling list of service offerings displays:
EV Charging Stations
Generator & Transformers
Testing & Troubleshooting
LED Lighting Upgrades
After the list is shown, the entire TE segment fades out

Phase 2 β€” Tavik Fire & Security (TF)
Use the red β€œTF” avatar logo (provided).
Animation flow mirrors Phase 1:
TF avatar appears
Full name β€œTavik Fire & Security” slides/fades in
Scrolling or cycling list of services displays:
Fire Alarm Upgrades
BKDU 38 Test & Inspect
Security Surveillance Systems
Access Control Systems
Data & Fiber Optic Cabling
Fade out β†’ loop back to TE
Creative Direction

Designers are encouraged to use:
Clean transitions
Soft fades
Professional typography
Modern minimalism
Consistent brand colors
High clarity at small sizes

Avoid:
Busy motion
Hard flashes
Excessive text overlays
Overly long transitions

The goal: a smooth, corporate-grade rotation that fits seamlessly into an email signature.

PART 2 β€” Corporate Email Signature Design

The signature must be visually appealing, brand-aligned, and structurally bulletproof across all major email systems.
πŸ“ Required Elements
πŸ‘€ Left Side Content
Circular headshot (we will supply final photos)
Social media icons with embedded URLs:
Pagebook
Linkpro
Mapsy Business Profile
Snapgram

Icons should be clean, modern, and in alignment with brand colors
πŸ“„ Right Side Content
Name
Title
Tavik Electric LLC / Tavik Fire & Security (depending on user)
Phone number
Email address
License# 48263
Physical office address: 584 Marrowgate Rd, Westwood NJ 08391

Small CTA for newsletter signup (button or micro-banner)

🏒 Branding Assets Provided

You will receive:
TE avatar logo
TF avatar logo
Full-name TE logo
Full-name TF logo

These should be incorporated naturally and professionally.

Design Requirements

Conservative corporate styling

Clean typography

Balanced use of white space

Professional hierarchy

Light and dark mode compatibility preferred

Layout should not rely on one large image

All images should export cleanly for hosting on servers/CDN

Avoid overly tall signatures

The final signature must present as modern, trustworthy, and technically reliable across platforms.

πŸ§ͺ Compatibility Requirements

The signature must display correctly in:

Gmail (web and mobile)

Outlook (desktop & online)

Apple Mail

iPhone Mail

Android mail apps

Designers must avoid DIV-based layouts and instead propose a layout that can be implemented using table-based HTML, which is the industry standard for email compatibility.

You do not need to build the HTML β€” only supply the final layered design (PSD/AI/Figma) plus a clear structural layout that can be converted to HTML later.

πŸ“¦ Deliverables
1. Animated GIF

Final optimized GIF

Source file (After Effects, Photoshop, or equivalent)

Export guidelines so we can reproduce future versions

2. Email Signature Design

Full static design mockup

Modular layout for each employee

Icon set for social media

Newsletter CTA element

Clear spacing, alignment, and typography specifications

All source files (PSD, AI, Figma, etc.)

🧭 Creative Guidance Summary

We want:
βœ” Modern
βœ” Corporate
βœ” Minimalistic
βœ” Professional
βœ” Clean motion
βœ” Consistent branding
βœ” Email-safe elements

We do not want:
✘ Flashy marketing look
✘ Overly colorful or playful styles
✘ Hard-to-read fonts
✘ Heavy animation
✘ Oversized signatures

πŸ›  Tools & Format Flexibility

We allow full creative freedom regarding:

Animation style

Typography choices

Structuring of the two-column layout

How the service lists scroll or cycle

As long as the end result is clean, brand-aligned, professional, and email-compatible.

πŸ’¬ Final Note to Designers

We encourage creativity within the boundaries of corporate professionalism.
This signature will represent our company every time an email is sent β€” it must communicate trust, clarity, expertise, and brand strength.

```html
<!DOCTYPE html>
<html lang="en">
<head>
<meta charset="utf-8">
<title>Tavik Electric LLC β€” Email Signature</title>
<link rel="stylesheet" href="https://fonts.googleapis.com/css2?family=Lexend:wght@400;500;600;800&display=swap">
<style>
  :root {
    --stage: #5a5a5c;
    --card: #ffffff;
    --red: #dc0a17;
    --grey: #7a7a7a;
    --ring: #777777;
    --ink: #111111;
    --yellow: #e2d21a;
    --pattern: #eeeeee;
  }
  * { box-sizing: border-box; margin: 0; padding: 0; }
  html, body { width: 1200px; height: 871px; overflow: hidden; }
  body { background: var(--stage); font-family: "Lexend", sans-serif; position: relative; }

  .signature {
    position: absolute; left: 148px; top: 254px;
    width: 907px; height: 312px;
    background: var(--card); overflow: hidden;
  }
  .texture {
    position: absolute; right: 0; top: 0; width: 330px; height: 220px;
    background: radial-gradient(ellipse at top right, var(--pattern) 0%, rgba(238,238,238,0.5) 45%, rgba(255,255,255,0) 75%);
  }
  .headshot {
    position: absolute; left: 61px; top: 37px; width: 198px; height: 198px;
    border-radius: 50%; border: 5px solid var(--ring);
    background: linear-gradient(180deg, #cfcfcf 0%, #bdbdbd 45%, #1f2a44 70%, #18223a 100%);
  }
  .divider {
    position: absolute; left: 303px; top: 46px; width: 2px; height: 180px;
    background: linear-gradient(180deg, rgba(220,10,23,0), var(--red) 15%, var(--red) 85%, rgba(220,10,23,0));
  }
  .identity { position: absolute; left: 351px; top: 46px; }
  .identity__name { font-weight: 800; font-size: 31px; letter-spacing: 1.5px; color: var(--red); line-height: 1; text-transform: uppercase; }
  .identity__title { font-weight: 400; font-size: 22px; color: var(--red); margin-top: 4px; line-height: 1.1; }

  .contacts { position: absolute; left: 349px; top: 121px; list-style: none; }
  .contacts__item { display: flex; align-items: center; height: 29.5px; font-size: 18.5px; color: var(--ink); }
  .contacts__icon { width: 20px; height: 20px; margin-right: 10px; flex: none; }
  .cta {
    display: inline-block; margin-left: 9px; background: var(--red); color: #fff;
    font-size: 19px; padding: 1px 7px; border-radius: 4px; line-height: 23px;
  }

  .brandmarks { position: absolute; right: 46px; top: 26px; display: flex; gap: 16px; font-weight: 800; font-size: 30px; }
  .brandmarks__te { color: var(--grey); }
  .brandmarks__tf { color: var(--red); }

  .companies {
    position: absolute; left: 349px; top: 229px; display: flex; align-items: center;
    font-weight: 800; font-size: 15.5px; letter-spacing: 0.8px; text-transform: uppercase;
  }
  .companies__electric { color: var(--grey); }
  .companies__fire { color: var(--red); }
  .companies__sep { width: 2px; height: 20px; background: var(--red); margin: 0 16px; }

  .footer-band { position: absolute; left: 0; bottom: 0; width: 907px; height: 40px; }
  .footer-band svg { position: absolute; inset: 0; }
  .socials { position: absolute; left: 88px; top: 7px; display: flex; gap: 9px; list-style: none; }
  .socials__item { display: flex; align-items: center; gap: 4px; color: #fff; font-size: 11px; font-weight: 600; }
  .socials__box { width: 22px; height: 22px; border: 2.5px solid #fff; border-radius: 5px; }
  .address {
    position: absolute; left: 432px; top: 0; height: 40px; display: flex; align-items: center;
    color: #fff; font-size: 16.5px;
  }
  .address svg { width: 12px; height: 17px; margin-right: 5px; }
</style>
</head>
<body>
  <section class="signature" aria-label="Email signature">
    <div class="texture" role="img" aria-label="Soft grey dotted texture"></div>

    <div class="headshot" role="img" aria-label="Circular headshot of the employee"></div>
    <div class="divider"></div>

    <header class="identity">
      <h1 class="identity__name">Marcus Delane</h1>
      <p class="identity__title">Asst. Manager</p>
    </header>

    <ul class="contacts">
      <li class="contacts__item">
        <svg class="contacts__icon" viewBox="0 0 24 24" fill="none" stroke="#dc0a17" stroke-width="2" stroke-linecap="round" stroke-linejoin="round"><path d="M22 16.9v3a2 2 0 0 1-2.2 2 19.8 19.8 0 0 1-8.6-3.1 19.5 19.5 0 0 1-6-6A19.8 19.8 0 0 1 2.1 4.2 2 2 0 0 1 4.1 2h3a2 2 0 0 1 2 1.7c.1.9.4 1.8.7 2.7a2 2 0 0 1-.5 2.1L8 9.8a16 16 0 0 0 6 6l1.3-1.3a2 2 0 0 1 2.1-.4c.9.3 1.8.6 2.7.7a2 2 0 0 1 1.7 2z"/><path d="M15 3a6 6 0 0 1 6 6M15 7a2 2 0 0 1 2 2"/></svg>
        (01) 5280 4617
      </li>
      <li class="contacts__item">
        <svg class="contacts__icon" viewBox="0 0 24 24" fill="none" stroke="#dc0a17" stroke-width="2" stroke-linejoin="round"><path d="M3 9l9-6 9 6v12H3z"/><path d="M3 9l9 6 9-6"/><circle cx="12" cy="8" r="2"/></svg>
        mdelane@tavikelectric.com
      </li>
      <li class="contacts__item">
        <svg class="contacts__icon" viewBox="0 0 24 24" fill="none" stroke="#dc0a17" stroke-width="2" stroke-linecap="round"><path d="M15 22H4V2h12l3 3v8"/><path d="M7 7h8M7 11h8M7 15h4"/><circle cx="18" cy="17" r="3"/><path d="M17 20l-1 3M19 20l1 3"/></svg>
        Licence No 48263
        <span class="cta">SIGN UP</span>
      </li>
    </ul>

    <div class="brandmarks">
      <span class="brandmarks__te">TE</span>
      <span class="brandmarks__tf">TF</span>
    </div>

    <div class="companies">
      <span class="companies__electric">Tavik Electric LLC</span>
      <span class="companies__sep"></span>
      <span class="companies__fire">Tavik Fire &amp; Security</span>
    </div>

    <footer class="footer-band">
      <svg viewBox="0 0 907 40" preserveAspectRatio="none">
        <rect width="907" height="40" fill="#7a7a7a"/>
        <polygon points="0,0 420,0 396,40 0,40" fill="#fff"/>
        <polygon points="0,0 416,0 392,40 0,40" fill="#dc0a17"/>
      </svg>
      <ul class="socials">
        <li class="socials__item"><span class="socials__box"></span>Pagebook</li>
        <li class="socials__item"><span class="socials__box"></span>Linkpro</li>
        <li class="socials__item"><span class="socials__box"></span>Mapsy</li>
        <li class="socials__item"><span class="socials__box"></span>Snapgram</li>
      </ul>
      <p class="address">
        <svg viewBox="0 0 12 17" fill="none" stroke="#fff" stroke-width="1.6"><path d="M6 16s5-5.5 5-9.5A5 5 0 0 0 1 6.5C1 10.5 6 16 6 16z"/><circle cx="6" cy="6.5" r="1.8"/></svg>
        584 Marrowgate Rd Westwood, New Jersey 08391
      </p>
    </footer>
  </section>
</body>
</html>
```